HTF!!! We need a modern professional website for a business litigation law firm.

We need a modern, clean, professional and uncomplicated website for a new business trial and litigation law firm called "Hallorand Trial Firm PLLC". Website must be mobile optimized for iPad and smartphone. The law firm specializes in counseling and representing large corporations, small businesses and entrepreneurs in and out of the courtroom. Lawyers in the firm serve as Florida counsel and trial counsel to organizations facing claims involving product liability, premises liability, professional liability, vehicle and transportation liability, warranty claims, construction defects and delay claims, complex business disputes, commercial litigation and bid disputes in State and Federal Courts. The website is mainly to provide information about the firm, and should include sections describing the firm, identifying the Industries Served and Areas of Practice ," a separate page identifying the "Professionals", a separate page for "Resources & Advisories," and a traveling "Connect With Us" button a site visitor can click on that will launch an email to the Firm's general email account. The website should allow us to easily modify the content on these pages, and let us add/modify links to external information sources. We will not sell anything or take payments through the website. We do need to be able to easily upload and update photographs of attorneys and add new attorneys names/email hyperlinks as the firm grows. We would like to add developments in the law or success stories easily and quickly, such as through a blog page. On the "Connect With Us" page the website should have hyperlinks to email the Firm, and there should be hyperlinks to email each professional on the "Professionals" page. The website should be viewable on mobile devices without distortion. The law firm focuses on trial work and should have some imagery associated with courtrooms, but the overall theme of the site should be modern, clean, and communicate sophistication and strength. The website should be made in Wordpress. We have uploaded logo files for Hallorand Trial Firm.

Target Market(s)

Corporations and companies that are looking for legal representation. Other attorneys/legal industry.

Industry/Entity Type

Legal Industry

Coding

Coded - Design and coding required

Number of Pages Required

1 page

Font styles to use
Sans Serif

Requirements
Must have
• Simple, clean, sophisticated, modern website that includes the logo, watermark of logo, and the elements described above.
Nice to have
• Pictures of city scape, buildings, courtroom, team members.

```html
<!DOCTYPE html>
<html lang="en">
<head>
<meta charset="utf-8">
<title>Hallorand Trial Firm PLLC</title>
<link href="https://fonts.googleapis.com/css2?family=Poppins:wght@400;500;600;700&family=Oswald:wght@600&family=Great+Vibes&display=swap" rel="stylesheet">
<style>
:root{
  --navy:#0f2a4a;
  --navy-deep:#0b1f38;
  --band:#1b3c69;
  --band-dark:#12294a;
  --tile:#143258;
  --sky:#b5dcf5;
  --ink:#1d2a3a;
  --muted:#4a5566;
  --gold:#f2b705;
  --white:#ffffff;
  --night:#16181d;
  --card-grey:#cfcfd1;
}
*{margin:0;padding:0;box-sizing:border-box}
html,body{width:1200px;height:3221px;overflow:hidden}
body{font-family:'Poppins',sans-serif;color:var(--ink);background:var(--white);position:relative}
section,header,footer{position:absolute;left:0;width:1200px}
.abs{position:absolute}
.btn{position:absolute;display:flex;align-items:center;justify-content:center;border:3px solid var(--navy);outline:2px solid #9fb4cc;outline-offset:-6px;background:var(--navy-deep);color:var(--white);font-size:14px;font-weight:500;border-radius:22px;letter-spacing:.2px;white-space:nowrap}
.eyebrow{position:absolute;left:0;width:1200px;text-align:center;font-size:15px;color:var(--navy)}
.heading{position:absolute;left:0;width:1200px;text-align:center;font-size:25px;font-weight:700;color:var(--navy)}
.ph{position:absolute}

.site-header{top:0;height:80px}
.brand{position:absolute;left:80px;top:18px;display:flex;align-items:center;gap:8px}
.brand-mark{width:14px;height:14px;background:var(--navy)}
.brand-name{font-size:15px;font-weight:700;color:var(--navy);line-height:1.05;width:110px}
.phone{position:absolute;right:80px;top:6px;font-family:'Oswald',sans-serif;font-size:19px;color:var(--navy-deep);display:flex;align-items:center;gap:8px}
.nav{position:absolute;top:49px;font-size:13px;color:var(--ink)}

.hero{top:80px;height:483px}
.hero-title{position:absolute;left:78px;top:135px;font-size:51px;color:var(--white);font-weight:400;letter-spacing:.5px}
.hero-text{position:absolute;left:81px;top:192px;width:480px;font-size:22.5px;line-height:30.5px;color:var(--white)}

.about-copy{position:absolute;left:676px;width:440px;font-size:14px;line-height:22px;color:var(--ink)}

.practice{top:1069px;height:475px;background:linear-gradient(120deg,#1e4577 0%,var(--band) 45%,var(--band-dark) 100%);overflow:hidden}
.tile{position:absolute;width:150px;height:154px;border:2px solid #0e2443;background:var(--tile);outline:1px solid #8eb0d6;outline-offset:-6px;color:var(--white);text-align:center}
.tile svg{position:absolute;left:45px;top:24px}
.tile-label{position:absolute;left:8px;right:8px;bottom:14px;font-size:13.5px;line-height:16.5px}
.tile.featured{background:#141414;outline:1px solid #c99a10;text-align:left}

.member{position:absolute;top:1695px;width:153px;height:253px;background:var(--sky);text-align:center}
.member .photo{position:absolute;left:0;top:0;width:153px;height:121px}
.member h3{position:absolute;top:124px;width:100%;font-size:14px;font-weight:700;color:#111}
.member .role{position:absolute;top:141px;width:100%;font-size:11.5px;font-weight:600;color:var(--navy)}
.member .bio{position:absolute;top:166px;left:8px;right:8px;font-size:11px;line-height:13px;color:#24324a;border-top:1px solid #8fbde0;padding-top:3px}
.member .links{position:absolute;top:220px;width:100%;display:flex;justify-content:center;gap:20px;align-items:center}
.soc{width:22px;height:18px;display:flex;align-items:center;justify-content:center}
.soc-box{width:16px;height:16px;border:2px solid #111;border-radius:3px}

.clients{top:2094px;height:375px;background:var(--night);overflow:hidden}
.client{position:absolute;top:64px;width:153px;height:211px;background:var(--sky);text-align:center}
.client .photo{position:absolute;left:0;top:0;width:153px;height:121px}
.client h3{position:absolute;top:127px;width:100%;font-size:14px;font-weight:700;color:#111}
.client p{position:absolute;top:148px;left:8px;right:8px;font-size:11.5px;line-height:15px;color:#24324a}
.clients-lead{position:absolute;left:102px;top:128px;color:#fff;font-size:19px;white-space:nowrap}
.clients-of{position:absolute;left:104px;top:176px;color:#fff;font-size:14px}
.clients-script{position:absolute;left:124px;top:154px;color:#fff;font-family:'Great Vibes',cursive;font-size:42px;line-height:50px;white-space:nowrap}

.post{position:absolute;top:2621px;width:330px;height:219px;background:var(--card-grey)}
.post .photo{position:absolute;left:0;top:0;width:153px;height:219px}
.post h3{position:absolute;left:169px;top:13px;font-size:20px;font-weight:400;color:#222}
.post .date{position:absolute;left:169px;top:41px;font-size:12px;color:#333}
.post p{position:absolute;left:169px;top:73px;width:150px;font-size:13.5px;line-height:20px;color:#444}
.post .btn{left:178px;top:169px;width:130px;height:32px;font-size:13px}

.site-footer{top:2985px;height:236px;background:linear-gradient(110deg,var(--navy-deep),#173965 70%,#0f2a4a)}
.f-head{position:absolute;font-size:17px;color:#7fb3e6;font-weight:500}
.f-link{position:absolute;font-size:13px;color:var(--white)}
</style>
</head>
<body>

<header class="site-header">
  <div class="brand"><span class="brand-mark"></span><span class="brand-name">HALLORAND TRIAL FIRM</span></div>
  <div class="phone">
    <svg width="20" height="20" viewBox="0 0 24 24" fill="none" stroke="#0b1f38" stroke-width="2.2"><path d="M5 3h4l2 5-2.5 1.5a11 11 0 0 0 6 6L16 13l5 2v4a2 2 0 0 1-2 2A17 17 0 0 1 3 5a2 2 0 0 1 2-2z"/></svg>
    555-210-0000
  </div>
  <nav>
    <span class="nav" style="left:543px">HOME</span>
    <span class="nav" style="left:621px">PROFESSIONALS</span>
    <span class="nav" style="left:764px">RESOURCES &amp; ADVISORIES</span>
    <span class="btn" style="left:958px;top:43px;width:161px;height:32px;font-size:13.5px">CONNECT WITH US</span>
  </nav>
</header>

<section class="hero" role="img" aria-label="City skyline at dusk with two smiling attorneys in business suits, arms crossed" style="background:linear-gradient(90deg,#2d261c 0%,#4a3a22 25%,#5b4c39 45%,#2c3b55 70%,#1c2b44 100%)">
  <div class="ph" style="left:660px;top:20px;width:540px;height:463px;background:radial-gradient(ellipse at 50% 55%,#203a68 0%,#17284a 55%,rgba(30,40,60,0) 80%)"></div>
  <h1 class="hero-title">LOREM IPSUM SEDO</h1>
  <p class="hero-text">Lorem ipsum dolor sit amet, consectetur adipiscing elit, sed do eiusmod tem pori incididunt ut labore et dolore magn agti</p>
  <span class="btn" style="left:235px;top:311px;width:157px;height:35px">CONNECT WITH US</span>
</section>

<section class="about" style="top:563px;height:506px">
  <div class="eyebrow" style="top:62px">ABOUT US</div>
  <h2 class="heading" style="top:86px">WELCOM HTF BUSINESS LITIGATION LAW FIRM</h2>
  <div class="ph" role="img" aria-label="Group of smiling attorneys holding folders" style="left:80px;top:152px;width:196px;height:289px;border-radius:8px 0 0 8px;background:linear-gradient(160deg,#d9d4cc,#6d6560 60%,#2a2a30)"></div>
  <div class="ph" role="img" aria-label="Attorneys standing in an office" style="left:276px;top:152px;width:134px;height:145px;border-radius:0 8px 0 0;background:linear-gradient(160deg,#e7e4de,#9a948c)"></div>
  <div class="ph" role="img" aria-label="Team meeting around a conference table" style="left:418px;top:152px;width:194px;height:145px;border-radius:6px;background:linear-gradient(160deg,#d8dde2,#5b6068)"></div>
  <div class="ph" role="img" aria-label="Business partners shaking hands at a meeting" style="left:282px;top:305px;width:330px;height:136px;border-radius:0 0 8px 0;background:linear-gradient(160deg,#c8ccd2,#7e8896 60%,#3d4048)"></div>
  <p class="about-copy" style="top:147px">Lorem ipsum dolor sit amet, consectetur adipiscing elit, sed do eiusmod tempor incididunt ut labore et dolore magna aliqua. Quis ipsum suspendisse ultrices gravida. Risus commodo viverra maecenas accumsan lacus vel facilisis.</p>
  <p class="about-copy" style="top:253px">Lorem ipsum dolor sit amet, consectetur adipiscing elit, sed do eiusmod tempor incididunt ut labore et dolore magna aliqua. Quis ipsum suspendisse ultrices gravida. Risus commodo viverra maecenas accumsan lacus vel facilisis.</p>
  <span class="btn" style="left:676px;top:358px;width:162px;height:40px">CONNECT WITH US</span>
</section>

<section class="practice">
  <svg class="abs" style="left:0;top:0" width="1200" height="475"><path d="M0 0H420C380 80 300 110 230 100C140 90 80 150 0 160Z" fill="#24518a" opacity=".45"/><path d="M1200 300C1100 330 1000 420 900 475H1200Z" fill="#0c2140" opacity=".5"/></svg>
  <div class="abs" style="left:0;width:452px;top:183px;text-align:center;color:#fff;font-size:15px">WHAT WE DO</div>
  <h2 class="abs" style="left:0;width:452px;top:208px;text-align:center;color:#fff;font-size:25px;font-weight:700">AREAS OF PRACTICE</h2>
  <span class="btn" style="left:147px;top:262px;width:157px;height:35px;border-color:#0e2443;background:#13294b">CONNECT WITH US</span>

  <div class="tile featured" style="left:435px;top:66px">
    <div class="abs" style="left:9px;top:14px;color:var(--gold);font-size:14px;font-weight:500">PREMISES LIABILITY</div>
    <div class="abs" style="left:9px;top:38px;width:135px;font-size:11.5px;line-height:15px">Lorem ipsum dolor sit amet, consectetur adipiscing elit.</div>
    <span class="btn" style="left:22px;top:109px;width:106px;height:26px;font-size:11px;border-color:#333;outline-color:#999;background:#111">LEARN MORE</span>
  </div>
  <div class="tile" style="left:612px;top:66px">
    <svg width="60" height="60" viewBox="0 0 60 60" fill="none" stroke="#fff" stroke-width="2"><path d="M22 10l16 6v14c0 12-8 20-16 24-8-4-16-12-16-24V16z"/><path d="M22 18l10 4v9c0 8-5 13-10 16-5-3-10-8-10-16v-9z"/><circle cx="46" cy="12" r="5"/><path d="M38 56V26h16v30M46 32v24"/></svg>
    <div class="tile-label">PROFESSIONAL LIABILITY</div>
  </div>
  <div class="tile" style="left:790px;top:66px">
    <svg width="60" height="60" viewBox="0 0 60 60" fill="none" stroke="#fff" stroke-width="2"><path d="M14 16h28v28H14M42 26h9l7 9v9h-16"/><circle cx="22" cy="46" r="5"/><circle cx="48" cy="46" r="5"/><path d="M2 22h9M4 30h8M2 38h10"/></svg>
    <div class="tile-label" style="bottom:8px">VEHICLE AND TRANSPORTATION LIABILITY</div>
  </div>
  <div class="tile" style="left:967px;top:66px">
    <svg width="60" height="60" viewBox="0 0 60 60" fill="none" stroke="#fff" stroke-width="2"><path d="M30 4l20 8v16c0 14-10 24-20 28-10-4-20-14-20-28V12z"/><path d="M20 30l8 8 14-16"/></svg>
    <div class="tile-label">WARRANTY CLAIMS</div>
  </div>

  <div class="tile" style="left:435px;top:254px">
    <svg width="60" height="60" viewBox="0 0 60 60" fill="none" stroke="#fff" stroke-width="2"><path d="M14 58V8M20 58V8M14 16h6M14 28h6M14 40h6M4 12h52M10 12L17 4l7 8M50 12v14M44 30h12l-2 8h-8z"/><path d="M8 58h40"/></svg>
    <div class="tile-label" style="bottom:8px">CONSTRUCTION DEFECTS &amp; DELAY CLAIMS</div>
  </div>
  <div class="tile" style="left:612px;top:254px">
    <svg width="60" height="60" viewBox="0 0 60 60" fill="none" stroke="#fff" stroke-width="2"><circle cx="14" cy="10" r="5"/><path d="M8 58V24h12v34M14 36v22"/><circle cx="42" cy="14" r="9"/><path d="M39 11a3 3 0 1 1 3 4v3M42 21v1"/><path d="M30 38h10v-4a3 3 0 0 1 6 0v4h10v18H30z"/></svg>
    <div class="tile-label" style="bottom:8px">COMPLEX BUSINESS DISPUTES</div>
  </div>
  <div class="tile" style="left:790px;top:254px">
    <svg width="60" height="60" viewBox="0 0 60 60" fill="none" stroke="#fff" stroke-width="2"><circle cx="30" cy="14" r="10"/><path d="M30 8v12M27 11h5M27 17h5"/><path d="M30 24v16M4 28c4 10 12 20 26 20s22-10 26-20M12 40l-6 10M48 40l6 10"/></svg>
    <div class="tile-label" style="bottom:8px">COMMERCIAL LITIGATION &amp; BID DISPUTES</div>
  </div>
  <div class="tile" style="left:967px;top:254px">
    <svg width="60" height="60" viewBox="0 0 60 60" fill="none" stroke="#fff" stroke-width="2"><circle cx="30" cy="22" r="16"/><path d="M30 2v4M30 38v4M10 22H6M54 22h-4"/><path d="M26 14l-4 10h8l-4 10"/><path d="M6 46l12-8 10 6 10-6 12 8-8 8H14z"/></svg>
    <div class="tile-label">PARTNERSHIP DISPUTES</div>
  </div>
</section>

<section class="team" style="top:1544px;height:550px">
  <div class="eyebrow" style="top:61px">MEET THE TEAM</div>
  <h2 class="heading" style="top:86px">EXPERIENCED ATTORNEYS</h2>
</section>

<article class="member" style="left:169px">
  <div class="photo" role="img" aria-label="Portrait of attorney David W." style="background:linear-gradient(180deg,#e6e7e9,#7a8394 70%,#1f2c44)"></div>
  <h3>DAVID W.</h3><div class="role">Lorem ipsum dolor</div>
  <p class="bio">Lorem ipsum dolor sit amet consectetur adip scing elit.</p>
  <div class="links"><span class="soc"><svg width="22" height="16" viewBox="0 0 22 16" fill="none" stroke="#111" stroke-width="2"><rect x="1" y="1" width="20" height="14"/><path d="M1 1l10 8 10-8"/></svg></span><span class="soc"><span class="soc-box"></span></span><span class="soc"><span class="soc-box" style="border-radius:50%"></span></span></div>
</article>
<article class="member" style="left:346px">
  <div class="photo" role="img" aria-label="Portrait of attorney Shofia R." style="background:linear-gradient(180deg,#c9b59c,#8c705a 70%,#4a3a30)"></div>
  <h3>SHOFIA R.</h3><div class="role">Lorem ipsum dolor</div>
  <p class="bio">Lorem ipsum dolor sit amet consectetur adip scing elit.</p>
  <div class="links"><span class="soc"><svg width="22" height="16" viewBox="0 0 22 16" fill="none" stroke="#111" stroke-width="2"><rect x="1" y="1" width="20" height="14"/><path d="M1 1l10 8 10-8"/></svg></span><span class="soc"><span class="soc-box"></span></span><span class="soc"><span class="soc-box" style="border-radius:50%"></span></span></div>
</article>
<article class="member" style="left:523px">
  <div class="photo" role="img" aria-label="Portrait of attorney Scarlett W." style="background:linear-gradient(180deg,#dce6e6,#9aa9ac 70%,#2a2e38)"></div>
  <h3>SCARLETT W.</h3><div class="role">Lorem ipsum dolor</div>
  <p class="bio">Lorem ipsum dolor sit amet consectetur adip scing elit.</p>
  <div class="links"><span class="soc"><svg width="22" height="16" viewBox="0 0 22 16" fill="none" stroke="#111" stroke-width="2"><rect x="1" y="1" width="20" height="14"/><path d="M1 1l10 8 10-8"/></svg></span><span class="soc"><span class="soc-box"></span></span><span class="soc"><span class="soc-box" style="border-radius:50%"></span></span></div>
</article>
<article class="member" style="left:701px">
  <div class="photo" role="img" aria-label="Portrait of attorney Barrett M." style="background:linear-gradient(180deg,#cfd2d6,#6e7480 70%,#1b2232)"></div>
  <h3>BARRETT M.</h3><div class="role">Lorem ipsum dolor</div>
  <p class="bio">Lorem ipsum dolor sit amet consectetur adip scing elit.</p>
  <div class="links"><span class="soc"><svg width="22" height="16" viewBox="0 0 22 16" fill="none" stroke="#111" stroke-width="2"><rect x="1" y="1" width="20" height="14"/><path d="M1 1l10 8 10-8"/></svg></span><span class="soc"><span class="soc-box"></span></span><span class="soc"><span class="soc-box" style="border-radius:50%"></span></span></div>
</article>
<article class="member" style="left:878px">
  <div class="photo" role="img" aria-label="Portrait of attorney Cameron S." style="background:linear-gradient(180deg,#e2e4e8,#8c93a2 70%,#2c3a58)"></div>
  <h3>CAMERON S.</h3><div class="role">Lorem ipsum dolor</div>
  <p class="bio">Lorem ipsum dolor sit amet consectetur adip scing elit.</p>
  <div class="links"><span class="soc"><svg width="22" height="16" viewBox="0 0 22 16" fill="none" stroke="#111" stroke-width="2"><rect x="1" y="1" width="20" height="14"/><path d="M1 1l10 8 10-8"/></svg></span><span class="soc"><span class="soc-box"></span></span><span class="soc"><span class="soc-box" style="border-radius:50%"></span></span></div>
</article>
<span class="btn" style="left:496px;top:1989px;width:208px;height:38px">VIEW ALL PROFESSIONALS</span>

<section class="clients">
  <div class="clients-lead">Just a few of our Thousands</div>
  <div class="clients-of">of</div>
  <div class="clients-script">Satisfied Clients</div>

  <article class="client" style="left:435px"><div class="photo" role="img" aria-label="Portrait of client Olivia R." style="background:linear-gradient(180deg,#f0f0f2,#b7bcc6)"></div><h3>OLIVIA R.</h3><p>Lorem ipsum dolor sit amet consectetur adip. scing elit.</p></article>
  <article class="client" style="left:611px"><div class="photo" role="img" aria-label="Portrait of client Henry Y." style="background:linear-gradient(180deg,#e8eef2,#9fb3c8)"></div><h3>HENRY Y.</h3><p>Lorem ipsum dolor sit amet consectetur adip.</p></article>
  <article class="client" style="left:789px"><div class="photo" role="img" aria-label="Portrait of client William M." style="background:linear-gradient(180deg,#d5dde0,#6f8796)"></div><h3>WILLIAM M.</h3><p>Lorem ipsum dolor sit amet consectetur adip.</p></article>
  <article class="client" style="left:966px"><div class="photo" role="img" aria-label="Portrait of client Evelyn M." style="background:linear-gradient(180deg,#eef1f3,#3d3f46)"></div><h3>EVELYN M.</h3><p>Lorem ipsum dolor sit amet consectetur adip.</p></article>

  <span class="abs" style="left:739px;top:298px;width:13px;height:13px;border-radius:50%;background:#fff"></span>
  <span class="abs" style="left:760px;top:298px;width:13px;height:13px;border-radius:50%;background:#bbb"></span>
  <span class="abs" style="left:781px;top:298px;width:13px;height:13px;border-radius:50%;background:#bbb"></span>
  <span class="abs" style="left:802px;top:298px;width:13px;height:13px;border-radius:50%;background:#bbb"></span>
</section>

<section class="blog" style="top:2469px;height:516px">
  <div class="eyebrow" style="top:61px">NEWS</div>
  <h2 class="heading" style="top:86px">READ OUR LATTEST BLOG</h2>
</section>
<article class="post" style="left:80px">
  <div class="photo" role="img" aria-label="Judge's gavel on a desk" style="background:linear-gradient(160deg,#e3b889,#8a5630 55%,#2b1b12)"></div>
  <h3>LOREM IPSUM</h3><div class="date">Date: 21-01-02025</div>
  <p>Lorem ipsum dol sit ame con sect tu con r adipiscing eli seid do eiusmod tempor</p>
  <span class="btn">LEARN MORE</span>
</article>
<article class="post" style="left:435px">
  <div class="photo" role="img" aria-label="Lawyer writing notes at a desk" style="background:linear-gradient(160deg,#f2f0ee,#9c9590 55%,#2c2a2a)"></div>
  <h3>LOREM IPSUM</h3><div class="date">Date: 21-01-02025</div>
  <p>Lorem ipsum dol sit ame con sect turyqi adipiscing eli sed do eiusmod tempor</p>
  <span class="btn">LEARN MORE</span>
</article>
<article class="post" style="left:789px">
  <div class="photo" role="img" aria-label="Hands on a laptop with digital legal scales" style="background:linear-gradient(160deg,#3c7be0,#163b8a 55%,#0a1530)"></div>
  <h3>LOREM IPSUM</h3><div class="date">Date: 21-01-02025</div>
  <p>Lorem ipsum dol sit ame con sect tururi adipiscing eli sed do eiusmod. tem porei</p>
  <span class="btn">LEARN MORE</span>
</article>
<span class="btn" style="left:496px;top:2883px;width:208px;height:38px">VIEW OUR ALL BLOG</span>

<footer class="site-footer">
  <div class="abs" style="left:82px;top:52px;display:flex;align-items:center;gap:8px"><span style="width:14px;height:14px;background:#fff"></span><span style="color:#fff;font-size:15px;font-weight:700;line-height:1.1;width:110px">HALLORAND TRIAL FIRM</span></div>
  <div class="abs" style="left:80px;top:123px;color:#fff;font-size:12px;letter-spacing:10px">FOLLOW US</div>
  <span class="abs" style="left:82px;top:150px;width:26px;height:26px;background:#2a7cc7;border-radius:3px"></span>
  <span class="abs" style="left:135px;top:150px;width:26px;height:26px;background:#fff;border-radius:3px"></span>
  <span class="abs" style="left:186px;top:150px;width:26px;height:26px;background:#3f6ec2;border-radius:3px"></span>

  <div class="f-head" style="left:466px;top:40px">LINK</div>
  <div class="f-link" style="left:474px;top:70px">Professionals</div>
  <div class="f-link" style="left:474px;top:104px">Resources &amp; Advisories</div>
  <div class="f-link" style="left:474px;top:138px">Connect With Us</div>

  <div class="f-head" style="left:878px;top:40px">CONTACT</div>
  <svg class="abs" style="left:879px;top:72px" width="12" height="16" viewBox="0 0 12 16" fill="#7fb3e6"><path d="M6 0a6 6 0 0 1 6 6c0 4-6 10-6 10S0 10 0 6a6 6 0 0 1 6-6zm0 3.5a2.5 2.5 0 1 0 0 5 2.5 2.5 0 0 0 0-5z"/></svg>
  <div class="f-link" style="left:900px;top:70px;width:180px;line-height:17px">Lorem ipsum dol sit ame con sect turuti adipis</div>
  <svg class="abs" style="left:878px;top:116px" width="15" height="15" viewBox="0 0 24 24" fill="none" stroke="#7fb3e6" stroke-width="2.4"><path d="M5 3h4l2 5-2.5 1.5a11 11 0 0 0 6 6L16 13l5 2v4a2 2 0 0 1-2 2A17 17 0 0 1 3 5a2 2 0 0 1 2-2z"/></svg>
  <div class="f-link" style="left:900px;top:114px">555-210-0000</div>
  <svg class="abs" style="left:878px;top:148px" width="16" height="12" viewBox="0 0 16 12" fill="none" stroke="#7fb3e6" stroke-width="1.6"><rect x="1" y="1" width="14" height="10"/><path d="M1 1l7 6 7-6"/></svg>
  <div class="f-link" style="left:900px;top:144px">admin@hallorand.example</div>

  <div class="abs" style="left:80px;top:196px;width:1040px;border-top:1px solid #34507a"></div>
  <div class="abs" style="left:0;width:1200px;top:207px;text-align:center;font-size:12px;color:#6f82a0">Copyright © 2025 HTF All right reserved.</div>
</footer>

</body>
</html>
```